Business Card Design

We require a business card design for a law firm, our signature colours are maroon and cream. Our slogan is "From our family to yours", we would like the cards to be professional however feminine at the same time.

Industry/Entity Type

Business

Contact Information for Business Card

Helena Brockett & Associates Lawyers & Conveyancers, Helena Brockett LL.B. Principal Solicitor, 17 Thornbury Street, Kelvale NSW 2239

Logo styles of interest
Emblem Logo
Abstract Logo
Wordmark Logo

```html
<!DOCTYPE html>
<html lang="en">
<head>
<meta charset="utf-8">
<title>Helena Brockett &amp; Associates – Business Card</title>
<link rel="stylesheet" href="https://fonts.googleapis.com/css2?family=EB+Garamond:wght@400;500;600&display=swap">
<style>
  :root {
    --maroon: #8e2a35;
    --cream: #fdebda;
    --ivory: #fff8f0;
    --ink: #8a2a33;
    --ink-soft: #93343c;
  }
  html, body {
    margin: 0;
    padding: 0;
    overflow: hidden;
    background: var(--cream);
  }
  .card {
    position: relative;
    width: 1200px;
    height: 695px;
    background: var(--cream);
    font-family: "EB Garamond", Garamond, serif;
    overflow: hidden;
  }
  .card__band {
    position: absolute;
    left: 0;
    top: 0;
    width: 1200px;
    height: 381px;
    background: var(--maroon);
  }
  .firm-name {
    position: absolute;
    left: 62px;
    top: 72px;
    margin: 0;
    font-size: 52px;
    font-weight: 600;
    line-height: 76px;
    color: var(--ivory);
    letter-spacing: 0.2px;
  }
  .emblem {
    position: absolute;
    left: 934px;
    top: 62px;
    width: 181px;
    height: 164px;
  }
  .slogan {
    position: absolute;
    left: 0;
    width: 1234px;
    top: 309px;
    margin: 0;
    text-align: center;
    font-size: 41px;
    font-weight: 400;
    line-height: 1;
    letter-spacing: 1px;
    color: var(--ivory);
  }
  .contact {
    position: absolute;
    left: 0;
    width: 1206px;
    text-align: center;
    margin: 0;
    line-height: 1;
  }
  .contact__name {
    top: 443px;
    font-size: 40px;
    font-weight: 600;
    color: var(--ink);
  }
  .contact__role {
    top: 507px;
    width: 1196px;
    font-size: 31px;
    font-weight: 400;
    color: var(--ink-soft);
  }
  .contact__address {
    top: 648px;
    width: 1208px;
    font-size: 24px;
    font-weight: 400;
    color: var(--ink-soft);
    word-spacing: 2px;
  }
</style>
</head>
<body>
  <div class="card">
    <div class="card__band"></div>

    <h1 class="firm-name">Helena Brockett &amp; Associates<br>Lawyers &amp; Conveyancers</h1>

    <svg class="emblem" role="img" aria-label="Emblem of ornate scales of justice" viewBox="0 0 181 164">
      <defs>
        <radialGradient id="emblemGlow" cx="50%" cy="50%" r="60%">
          <stop offset="0%" stop-color="#fff8f0" stop-opacity="0.32"/>
          <stop offset="100%" stop-color="#fff8f0" stop-opacity="0.12"/>
        </radialGradient>
      </defs>
      <rect x="0" y="0" width="181" height="164" rx="10" fill="url(#emblemGlow)"/>
    </svg>

    <p class="slogan">FROM OUR FAMILY&nbsp; TO YOURS</p>

    <p class="contact contact__name">Helena Brockett LL.B.</p>
    <p class="contact contact__role">Principal Solicitor</p>
    <p class="contact contact__address">17 Thornbury Street,&nbsp; Kelvale NSW 2239</p>
  </div>
</body>
</html>
```